Quandoria Tours - Astronomy in the Kimberley

Quandoria Tours requires a web page to advertise astronomy tours in the East Kimberley, Australia. It needs the following tabs - Home, Tours, Astronomy Events, Gallery, Testimonials, Contacts.

It should target tourists to the Kimberley.
We are unsure of which colours to go with at the moment but we have included our logo if it helps.

It should be mobile and tablet friendly.

Target Market(s)

Families, +40, Tourist, hobby astronomists,

Industry/Entity Type

Events

Number of Pages Required

3 page

Colors
3377b5
ffffff

Requirements
Must have
• Home, Tours, Astronomy Events, Gallery, Calendar, Testimonials, Contacts.
• 'Quandoria Tours' logo
Nice to have
• Pictures of portable amateur telescopes. Pictures of Lake Kununurra or Wyndham.
Should not have
• Pictures of extremely large professional telescopes.

```html
<!DOCTYPE html>
<html lang="en">
<head>
<meta charset="utf-8">
<title>Quandoria Tours – Astronomy in the Kimberley</title>
<link href="https://fonts.googleapis.com/css2?family=Lato:ital,wght@0,400;0,700;1,400;1,700&family=Source+Sans+3:wght@400;600&family=Tinos:wght@700&display=swap" rel="stylesheet">
<style>
:root{
  --brand:#3377b5;
  --brand-dark:#2a62a0;
  --brand-deep:#1f4f85;
  --sky-light:#bcd8f3;
  --ink:#222;
  --muted:#555;
  --white:#fff;
  --night:#000;
  --footer:#3a7cc0;
}
*{box-sizing:border-box;margin:0;padding:0}
html,body{width:1200px;height:2299px;overflow:hidden;background:var(--white)}
body{font-family:"Lato",sans-serif;color:var(--ink);position:relative}
.page{position:relative;width:1200px;height:2299px;overflow:hidden}
.abs{position:absolute}
a{color:inherit;text-decoration:none}

/* hero */
.hero{left:0;top:0;width:1200px;height:650px;
  background:linear-gradient(180deg,#1a1d3a 0%,#3b3f6e 25%,#5d5a86 40%,#8f6f80 52%,#e39a55 58%,#3a4a6a 63%,#2a2f3d 72%,#3a3130 100%)}
.hero-curve{left:0;top:590px;width:1200px;height:60px}
.logo{left:132px;top:0;width:233px;height:207px;background:var(--white);
  display:flex;align-items:flex-end;justify-content:center;padding-bottom:40px;gap:8px}
.logo-dot{width:14px;height:14px;border-radius:50%;background:var(--brand)}
.logo-name{font-family:"Lato",sans-serif;font-weight:700;font-size:22px;color:var(--brand)}
.call{left:889px;top:18px;display:flex;gap:12px;align-items:center;color:var(--white)}
.call-icon{width:34px;height:34px;border-radius:50%;border:2px solid var(--white);background:var(--brand);display:flex;align-items:center;justify-content:center}
.call-label{font-size:13px;font-weight:700;color:#7cc0f2;line-height:1}
.call-number{font-size:19px;font-weight:700;line-height:1.3}
.nav{top:84px;left:0;width:1200px;height:24px}
.nav a{position:absolute;top:0;transform:translateX(-50%);color:var(--white);font-weight:700;font-size:14px;white-space:nowrap}
.caption{left:132px;top:274px;width:479px;height:232px;background:rgba(255,255,255,.3);padding:14px 16px}
.caption h1{font-size:29px;line-height:38px;font-style:italic;font-weight:700;color:var(--brand-dark)}
.caption p{margin-top:10px;font-size:18px;line-height:26px;font-style:italic;font-weight:700;color:var(--white)}
.dots{left:565px;top:631px;display:flex;gap:4px}
.dots span{width:15px;height:15px;border-radius:50%;background:#c6c6c6;border:1px solid #999}
.dots span.on{background:var(--brand)}

/* welcome */
.welcome-title{left:132px;top:708px;display:flex;align-items:center;gap:14px;font-family:"Source Sans 3",sans-serif;font-size:28px;color:#444}
.welcome-title em{font-style:normal;color:var(--brand)}
.mark{width:44px;height:20px;border-radius:50%;background:var(--brand)}
.title-rule{left:132px;top:751px;width:552px;height:3px;background:linear-gradient(90deg,#bbb,#eee)}
.welcome-text{left:132px;top:764px;width:555px;font-size:14px;line-height:24px;color:var(--ink)}
.btn{display:inline-flex;align-items:center;justify-content:center;background:var(--brand);color:var(--white);font-weight:700;font-size:13px;border-radius:2px;box-shadow:0 1px 2px rgba(0,0,0,.3)}
.welcome-btn{left:132px;top:917px;width:98px;height:29px}
.video{left:722px;top:713px;width:348px;height:219px;background:var(--white);box-shadow:0 0 6px rgba(0,0,0,.25);padding:6px}
.video-frame{width:100%;height:100%;background:linear-gradient(180deg,#0b1a3c,#1c3a78 55%,#0a1326);position:relative}
.video-bar{position:absolute;left:0;bottom:0;width:100%;height:30px;background:rgba(20,20,20,.85);display:flex;align-items:center;gap:10px;padding:0 10px;color:var(--white);font-size:12px}
.track{flex:1;height:5px;background:#ccc;position:relative}
.track i{position:absolute;left:40%;width:25%;height:100%;background:var(--brand)}
.video-note{left:722px;top:938px;width:332px;text-align:right;font-style:italic;font-size:21px;color:var(--brand-dark)}

/* tours */
.tours{left:0;top:978px;width:1200px;height:427px;background:linear-gradient(180deg,#2d6ba7,#3a80bd 50%,#2f6aa4)}
.tours-title{left:0;top:1005px;width:1200px;text-align:center;font-family:"Source Sans 3",sans-serif;font-size:26px;color:var(--white)}
.tours-rule{top:1021px;height:3px;width:360px;background:repeating-linear-gradient(90deg,rgba(255,255,255,.45) 0 2px,transparent 2px 4px)}
.arrow{top:1176px;width:36px;height:32px}
.card{top:1062px;width:205px;height:307px;background:var(--white);padding:8px;box-shadow:3px 3px 0 #e8e8e8,6px 6px 0 #cfcfcf,0 2px 6px rgba(0,0,0,.4)}
.card-photo{height:148px;background:linear-gradient(180deg,#0d1f44,#28508f 70%,#50463a)}
.card-place{margin-top:8px;text-align:center;font-size:15px;color:var(--brand)}
.card-region{margin-top:6px;border-top:1px dotted #bbb;padding-top:8px;text-align:center;font-size:16px;color:var(--ink)}
.card-text{margin-top:8px;border-top:1px dotted #bbb;padding-top:8px;font-size:11.5px;line-height:16px;color:#333}
.card-meta{position:absolute;left:8px;right:8px;bottom:10px;display:flex;justify-content:space-between;font-size:12px;color:#333}

/* columns */
.col-title{top:1445px;font-family:"Source Sans 3",sans-serif;font-size:20px;color:#444}
.col-title em{font-style:normal;color:var(--brand)}
.col-rule{top:1481px;height:4px;background:repeating-linear-gradient(135deg,#ccc 0 1px,transparent 1px 3px)}
.col-text{font-size:13.5px;line-height:23px;color:#333}
.weather-bar{left:132px;top:1583px;width:280px;height:29px;background:var(--brand-dark);color:var(--white);font-weight:700;font-size:14px;display:flex;align-items:center;justify-content:space-between;padding:0 18px}
.weather-panel{left:132px;top:1612px;width:280px;height:111px;background:var(--sky-light)}
.sun{left:152px;top:1637px;width:26px;height:26px;border-radius:50%;background:radial-gradient(circle,#ffd24a,#f0a20f)}
.weather-desc{left:193px;top:1641px;font-size:12px;color:#333}
.temp{left:152px;top:1683px;font-size:19px;font-weight:700;color:#333}
.temp small{font-size:11px;font-weight:400}
.weather-mark{left:300px;top:1658px;width:84px;height:38px;border-radius:50%;background:rgba(51,119,181,.35)}
.col-btn{top:1741px;width:86px;height:25px;font-size:12px}
.shot{width:139px;height:106px;background:linear-gradient(180deg,#1c3f88,#4b7ad0 55%,#0c0e18 80%)}
.event-date{font-size:13px;color:#666}
.event-title{font-size:13px;font-weight:700;color:var(--brand)}
.event-body{font-size:12px;line-height:17px;color:#444}
.event-sep{left:788px;top:1616px;width:282px;border-top:1px dashed #bbb}

/* moon phase */
.moon{left:0;top:1801px;width:1200px;height:211px;background:var(--night);color:var(--white)}
.moon-title{left:132px;top:1816px;font-family:"Source Sans 3",sans-serif;font-size:21px;color:var(--white)}
.select{top:1853px;height:24px;background:var(--white);border:1px solid #aaa;font-size:12px;color:#333;display:flex;align-items:center;padding-left:8px}
.select b{position:absolute;right:0;top:0;width:24px;height:22px;background:var(--brand)}
.go{left:374px;top:1853px;width:28px;height:24px;border:1px solid #aaa;background:var(--brand);color:var(--white);font-size:11px;font-weight:700;display:flex;align-items:center;justify-content:center}
.moon-note{left:423px;top:1857px;font-size:12px;color:var(--white)}
.cal{left:130px;top:1893px;width:938px;height:97px;background:var(--white);border-radius:6px}
.cal-nav{top:1926px;width:20px;height:28px;background:var(--white);border-radius:3px}
.day{top:1897px;width:58px;height:89px;border:1px solid #777;background:var(--white)}
.day-name{height:20px;border-bottom:1px solid #777;text-align:center;font-family:"Tinos",serif;font-size:13px;color:#111;line-height:19px}
.day-num{position:absolute;left:3px;top:21px;font-family:"Tinos",serif;font-size:13px;color:#111}
.day-moon{position:absolute;left:8px;top:36px;width:44px;height:44px;border-radius:50%;background:radial-gradient(circle at 40% 40%,#eee,#9a9a9a 70%,#555)}

/* footer */
.footer{left:0;top:2012px;width:1200px;height:287px;background:linear-gradient(180deg,#3f82c4,#3574b6)}
.foot-rule{left:0;top:2072px;width:1200px;border-top:1px dashed rgba(255,255,255,.5)}
.foot-div{top:2082px;width:1px;height:200px;background:rgba(255,255,255,.3)}
.foot-title{top:2027px;font-family:"Source Sans 3",sans-serif;font-weight:600;font-size:21px;color:var(--white)}
.links{left:130px;top:2088px;list-style:none}
.links li{font-size:13px;line-height:23.6px;color:var(--white)}
.links li::before{content:"›";margin-right:10px;font-weight:700}
.field{left:317px;width:221px;background:var(--white);border:1px solid #bbb;font-size:12px;font-style:italic;color:#999;padding:5px 8px}
.submit{left:319px;top:2244px;width:96px;height:28px;background:linear-gradient(#eee,#bbb);border:1px solid #888;color:#333;font-weight:700;font-size:13px;display:flex;align-items:center;justify-content:center}
.contact{left:598px;top:2088px;font-size:13px;line-height:19px;color:var(--white)}
.contact-line{left:598px;display:flex;align-items:center;gap:10px;font-size:13px;color:var(--white)}
.social{top:2012px;width:30px;height:30px;border-radius:50%;margin-top:15px}
.foot-name{left:830px;top:2110px;font-family:"Lato",sans-serif;font-weight:700;font-size:36px;color:rgba(255,255,255,.15)}
.copy{left:820px;top:2233px;width:255px;text-align:center;font-size:12.5px;line-height:18px;color:var(--white)}
</style>
</head>
<body>
<div class="page">

  <!-- hero -->
  <div class="abs hero" role="img" aria-label="Night sky over a rocky coastline at sunset, a stargazer at a portable telescope beside a campervan"></div>
  <svg class="abs hero-curve" viewBox="0 0 1200 60" preserveAspectRatio="none" aria-hidden="true">
    <path d="M0 50 Q600 -40 1200 50 L1200 60 L0 60 Z" fill="#fff"/>
  </svg>
  <div class="abs logo"><span class="logo-dot"></span><span class="logo-name">Quandoria Tours</span></div>
  <div class="abs call">
    <div class="call-icon">
      <svg width="16" height="16" viewBox="0 0 24 24" aria-hidden="true"><path fill="#fff" d="M6.6 10.8a15 15 0 0 0 6.6 6.6l2.2-2.2c.3-.3.7-.4 1-.2 1.1.4 2.3.6 3.6.6.6 0 1 .4 1 1V20c0 .6-.4 1-1 1A17 17 0 0 1 3 4c0-.6.4-1 1-1h3.5c.6 0 1 .4 1 1 0 1.3.2 2.5.6 3.6.1.3 0 .7-.2 1z"/></svg>
    </div>
    <div><div class="call-label">Call Now</div><div class="call-number">+123 456 7890</div></div>
  </div>
  <nav class="abs nav">
    <a href="#" style="left:455px;top:-4px" aria-label="Home"><svg width="24" height="22" viewBox="0 0 24 22"><path fill="#3aa0e0" d="M12 1 1 11h3v10h6v-6h4v6h6V11h3z"/></svg></a>
    <a href="#" style="left:547px">About Us</a>
    <a href="#" style="left:650px">Tours</a>
    <a href="#" style="left:780px">Astronomy Events</a>
    <a href="#" style="left:917px">Gallery</a>
    <a href="#" style="left:1030px">Contact Us</a>
  </nav>
  <div class="abs caption">
    <h1>Lorem ipsum dolor sit amet, consectetur adipiscing elit.</h1>
    <p>Lorem ipsum dolor sit amet, consecttur adipiscing elit. Vivamus interdum diam ante, sed vtpat ligula viverra ac. Interdum et malesuada fames ac ante ipsum primis in faucibus.</p>
  </div>
  <div class="abs dots"><span class="on"></span><span></span><span></span><span></span></div>

  <!-- welcome -->
  <h2 class="abs welcome-title"><span class="mark"></span><span>Welcome to <em>Quandoria Tours</em></span></h2>
  <div class="abs title-rule"></div>
  <p class="abs welcome-text">Lorem ipsum dolor sit amet, consectetur adipiscing elit. Vivamus interdum diam ante, sed volutpat ligula viverra ac. Interdum et malesuada fames ac ante ipsum primis in faucibus. Cras elementum lacus non neque finibus, eget finibus dui viverra. Ut eleifend, orci eu rutrum vulputate, lectus tortor dictum mauris, vel pharetra neque felis tincidunt nibh. Proin gravida, libero sed pellentesque aliquet, purus dolor suscipit lorem, quis vulputate dolor lacus at erat. Cras sit amet felis ac quam interdum aliquet vitae eget est.</p>
  <a href="#" class="abs btn welcome-btn">Read more »</a>
  <div class="abs video">
    <div class="video-frame" role="img" aria-label="Intro video still: lit tent under the Milky Way between trees">
      <div class="video-bar">
        <svg width="12" height="12" viewBox="0 0 12 12"><path fill="#fff" d="M2 1l9 5-9 5z"/></svg>
        <span class="track"><i></i></span>
        <span>|||||| HD</span>
      </div>
    </div>
  </div>
  <p class="abs video-note">Please watch intro video.</p>

  <!-- tours -->
  <div class="abs tours" role="img" aria-label="Blue-toned band with silhouetted trees"></div>
  <div class="abs tours-rule" style="left:132px"></div>
  <div class="abs tours-rule" style="left:708px"></div>
  <h2 class="abs tours-title">Our Tours</h2>
  <svg class="abs arrow" style="left:70px" viewBox="0 0 36 32" aria-hidden="true"><path d="M34 16H4M16 4 4 16l12 12" stroke="#fff" stroke-width="3" fill="none"/></svg>
  <svg class="abs arrow" style="left:1094px" viewBox="0 0 36 32" aria-hidden="true"><path d="M2 16h30M20 4l12 12-12 12" stroke="#fff" stroke-width="3" fill="none"/></svg>

  <article class="abs card" style="left:139px">
    <div class="card-photo" role="img" aria-label="Star trails above a campervan and hill"></div>
    <h3 class="card-place">Kununurra</h3>
    <p class="card-region">East Kimberley</p>
    <p class="card-text">Lorem ipsum dolor sit amet consec tetur adipiscing elit.</p>
    <div class="card-meta"><span>$7000</span><span>8 days</span></div>
  </article>
  <article class="abs card" style="left:379px">
    <div class="card-photo" role="img" aria-label="Circular star trails over an observatory"></div>
    <h3 class="card-place">Lake Argyle</h3>
    <p class="card-region">East Kimberley</p>
    <p class="card-text">Lorem ipsum dolor sit amet consec tetur adipiscing elit.</p>
    <div class="card-meta"><span>$7000</span><span>8 days</span></div>
  </article>
  <article class="abs card" style="left:618px">
    <div class="card-photo" role="img" aria-label="Lighthouse under the Milky Way"></div>
    <h3 class="card-place">Wyndham</h3>
    <p class="card-region">East Kimberley</p>
    <p class="card-text">Lorem ipsum dolor sit amet consec tetur adipiscing elit.</p>
    <div class="card-meta"><span>$7000</span><span>8 days</span></div>
  </article>
  <article class="abs card" style="left:857px">
    <div class="card-photo" role="img" aria-label="Lit tent under a starry sky"></div>
    <h3 class="card-place">Halls Creek</h3>
    <p class="card-region">East Kimberley</p>
    <p class="card-text">Lorem ipsum dolor sit amet consec tetur adipiscing elit.</p>
    <div class="card-meta"><span>$7000</span><span>8 days</span></div>
  </article>

  <!-- weather -->
  <h2 class="abs col-title" style="left:132px">Weather <em>Forcast</em></h2>
  <div class="abs col-rule" style="left:132px;width:280px"></div>
  <p class="abs col-text" style="left:132px;top:1502px;width:280px">Lorem ipsum dolor sit amet, consectetur adipiscing elit. Vivamus interdum diam ante sed volutpat ligula viverra ac.</p>
  <div class="abs weather-bar"><span>MAR-16-2015</span><span>‹ ›</span></div>
  <div class="abs weather-panel"></div>
  <div class="abs sun"></div>
  <div class="abs weather-desc">Mostly Sunny</div>
  <div class="abs temp">31<sup>°</sup> <small>Lo 14<sup>°</sup></small></div>
  <div class="abs weather-mark"></div>
  <a href="#" class="abs btn col-btn" style="left:326px">Read more</a>

  <!-- gallery -->
  <h2 class="abs col-title" style="left:460px">View <em>Gallery</em></h2>
  <div class="abs col-rule" style="left:460px;width:285px"></div>
  <div class="abs shot" style="left:460px;top:1505px" role="img" aria-label="Silhouetted stargazers at twilight"></div>
  <div class="abs shot" style="left:605px;top:1505px" role="img" aria-label="Campervan under the night sky"></div>
  <div class="abs shot" style="left:460px;top:1617px" role="img" aria-label="Silhouettes with a portable telescope"></div>
  <div class="abs shot" style="left:605px;top:1617px" role="img" aria-label="Stargazers pointing at the Milky Way"></div>
  <a href="#" class="abs btn col-btn" style="left:662px">Read more</a>

  <!-- events -->
  <h2 class="abs col-title" style="left:788px">Astronomy <em>Events</em></h2>
  <div class="abs col-rule" style="left:788px;width:282px"></div>
  <div class="abs" style="left:788px;top:1528px;width:282px">
    <p class="event-date">03 Mar 2015</p>
    <p class="event-title">Lorem ipsum dolor sit amet, molding.</p>
    <p class="event-body">Duis autem vel eum iriure dolor in hendrerit vulputate velit esse molestie consequat. iriure dolor in hendrer</p>
  </div>
  <div class="abs event-sep"></div>
  <div class="abs" style="left:788px;top:1625px;width:282px">
    <p class="event-date">03 Mar 2015</p>
    <p class="event-title">Lorem ipsum dolor sit amet, molding.</p>
    <p class="event-body">Duis autem vel eum iriure dolor in hendrerit vulputate velit esse molestie consequat.</p>
  </div>
  <a href="#" class="abs btn col-btn" style="left:984px">Read more</a>

  <!-- moon phase -->
  <div class="abs moon"></div>
  <h2 class="abs moon-title">Moon Phase</h2>
  <div class="abs select" style="left:132px;width:110px">MAR<b></b></div>
  <div class="abs select" style="left:254px;width:111px">2015<b></b></div>
  <div class="abs go">GO</div>
  <p class="abs moon-note"><b>Note:</b>Lorem ipsum dolor sit amet, consectetuer adipiscing elit, sed diam nonummy nibh euismod almet Lorem</p>
  <div class="abs cal"></div>
  <div class="abs cal-nav" style="left:120px"><svg width="20" height="28" viewBox="0 0 20 28"><path d="M13 8 7 14l6 6" stroke="#000" stroke-width="2" fill="none"/></svg></div>
  <div class="abs cal-nav" style="left:1059px"><svg width="20" height="28" viewBox="0 0 20 28"><path d="M7 8l6 6-6 6" stroke="#000" stroke-width="2" fill="none"/></svg></div>

  <div class="abs day" style="left:144px"><div class="day-name">Sun</div><span class="day-num">1</span><span class="day-moon" role="img" aria-label="Moon phase"></span></div>
  <div class="abs day" style="left:210px"><div class="day-name">Mon</div><span class="day-num">2</span><span class="day-moon" role="img" aria-label="Moon phase"></span></div>
  <div class="abs day" style="left:276px"><div class="day-name">Tue</div><span class="day-num">3</span><span class="day-moon" role="img" aria-label="Moon phase"></span></div>
  <div class="abs day" style="left:342px"><div class="day-name">Wed</div><span class="day-num">4</span><span class="day-moon" role="img" aria-label="Moon phase"></span></div>
  <div class="abs day" style="left:408px"><div class="day-name">Thu</div><span class="day-num">5</span><span class="day-moon" role="img" aria-label="Moon phase"></span></div>
  <div class="abs day" style="left:474px"><div class="day-name">Fri</div><span class="day-num">6</span><span class="day-moon" role="img" aria-label="Moon phase"></span></div>
  <div class="abs day" style="left:540px"><div class="day-name">Sat</div><span class="day-num">7</span><span class="day-moon" role="img" aria-label="Moon phase"></span></div>
  <div class="abs day" style="left:606px"><div class="day-name">Sun</div><span class="day-num">8</span><span class="day-moon" role="img" aria-label="Moon phase"></span></div>
  <div class="abs day" style="left:672px"><div class="day-name">Mon</div><span class="day-num">9</span><span class="day-moon" role="img" aria-label="Moon phase"></span></div>
  <div class="abs day" style="left:738px"><div class="day-name">Tue</div><span class="day-num">10</span><span class="day-moon" role="img" aria-label="Moon phase"></span></div>
  <div class="abs day" style="left:804px"><div class="day-name">Wed</div><span class="day-num">11</span><span class="day-moon" role="img" aria-label="Moon phase"></span></div>
  <div class="abs day" style="left:870px"><div class="day-name">Thu</div><span class="day-num">12</span><span class="day-moon" role="img" aria-label="Moon phase"></span></div>
  <div class="abs day" style="left:936px"><div class="day-name">Fri</div><span class="day-num">13</span><span class="day-moon" role="img" aria-label="Moon phase"></span></div>
  <div class="abs day" style="left:1002px"><div class="day-name">Sat</div><span class="day-num">14</span><span class="day-moon" role="img" aria-label="Moon phase"></span></div>

  <!-- footer -->
  <footer class="abs footer"></footer>
  <div class="abs foot-rule"></div>
  <div class="abs foot-div" style="left:288px"></div>
  <div class="abs foot-div" style="left:570px"></div>
  <div class="abs foot-div" style="left:797px"></div>

  <h2 class="abs foot-title" style="left:133px">Quick Links</h2>
  <ul class="abs links">
    <li>Home</li><li>About Us</li><li>Tours</li><li>Astronomy Events</li><li>Gallery</li><li>Contact Us</li>
  </ul>

  <h2 class="abs foot-title" style="left:319px">Quick Inquiry</h2>
  <div class="abs field" style="top:2094px;height:29px">Name</div>
  <div class="abs field" style="top:2132px;height:29px">Email</div>
  <div class="abs field" style="top:2169px;height:66px">Message</div>
  <div class="abs submit">SUBMIT</div>

  <h2 class="abs foot-title" style="left:598px">Contact Details</h2>
  <p class="abs contact"><b>Quandoria Tours</b><br>16 Lorem ipsum dolor sit&nbsp; sed<br>benetion, Street no-123456</p>
  <div class="abs contact-line" style="top:2169px">
    <svg width="14" height="14" viewBox="0 0 24 24" aria-hidden="true"><path fill="#fff" d="M6.6 10.8a15 15 0 0 0 6.6 6.6l2.2-2.2c.3-.3.7-.4 1-.2 1.1.4 2.3.6 3.6.6.6 0 1 .4 1 1V20c0 .6-.4 1-1 1A17 17 0 0 1 3 4c0-.6.4-1 1-1h3.5c.6 0 1 .4 1 1 0 1.3.2 2.5.6 3.6.1.3 0 .7-.2 1z"/></svg>+123 456 7890</div>
  <div class="abs contact-line" style="top:2212px">
    <svg width="14" height="14" viewBox="0 0 24 24" aria-hidden="true"><path fill="#fff" d="M6 2h12v6H6zM3 9h18v9h-3v4H6v-4H3zm5 6v5h8v-5z"/></svg>+123 456 7890</div>
  <div class="abs contact-line" style="top:2253px">
    <svg width="14" height="12" viewBox="0 0 24 18" aria-hidden="true"><path fill="#fff" d="M0 0h24v18H0zm2 2v1l10 7 10-7V2z"/></svg>info@quandoriatours.com</div>

  <span class="abs social" style="left:926px;background:#3b5a9a"></span>
  <span class="abs social" style="left:964px;background:#3fb6e8"></span>
  <span class="abs social" style="left:1001px;background:#d93a2b"></span>
  <span class="abs social" style="left:1038px;background:#f08a24"></span>

  <div class="abs foot-name">Quandoria Tours</div>
  <p class="abs copy">© Copyright 2015 Quandoria Tours<br>All Rights Reserved</p>
</div>
</body>
</html>
```